Coralvale Meat Traders Business Cards

We require business cards revamped with our logo. A few details we would like to use.

1. Round Edges
2. Our logo over the top of a wagyu cattle background photo on one side of the card

Other side of the card has the below details.

1. Person Name (First & Last)
2. Job Position
3. Mobile Number
4. Email Address
5. Website Address

Simple & Neat.

Target Market(s)

Sales

Industry/Entity Type

Agriculture

Contact Information for Business Card

CORALVALE MEAT TRADERS

Colors

Designer to choose colors to be used in the design.

Requirements
Must have
• Company Logo

```html
<!DOCTYPE html>
<html lang="en">
<head>
<meta charset="utf-8">
<title>Coralvale Meat Traders – Business Cards</title>
<link href="https://fonts.googleapis.com/css2?family=Cinzel:wght@500;600&family=Montserrat:wght@400;500&display=swap" rel="stylesheet">
<style>
  :root {
    --maroon: #650d26;
    --maroon-light: #7a1630;
    --red: #8c1a1f;
    --white: #ffffff;
    --page: #e9e7e6;
    --shadow: rgba(0,0,0,0.18);
  }
  * { margin: 0; padding: 0; box-sizing: border-box; }
  html, body { width: 1200px; height: 939px; overflow: hidden; }
  body { background: var(--page); position: relative; font-family: "Montserrat", sans-serif; }

  .card {
    position: absolute;
    width: 540px; height: 310px;
    border-radius: 26px;
    overflow: hidden;
    box-shadow: 0 10px 26px var(--shadow);
  }
  .card--back { left: 60px; top: 120px; background: var(--maroon); }
  .card--front { left: 600px; top: 500px; background: var(--white); }

  /* Company name mark */
  .brand { position: absolute; display: flex; align-items: center; gap: 12px; }
  .brand__dot { border-radius: 50%; flex: none; }
  .brand__name {
    font-family: "Cinzel", serif; font-weight: 600;
    line-height: 1.05; letter-spacing: 0.04em;
  }
  .card--back .brand { left: 50%; top: 50%; transform: translate(-50%, -50%); }
  .card--back .brand__dot { width: 46px; height: 46px; border: 2px solid var(--maroon-light); }
  .card--back .brand__name { color: var(--maroon-light); font-size: 34px; }

  .card--front .brand { left: 34px; top: 92px; }
  .card--front .brand__dot { width: 30px; height: 30px; border: 2px solid var(--maroon); }
  .card--front .brand__name { color: var(--maroon); font-size: 21px; }

  .wave { position: absolute; inset: 0; width: 100%; height: 100%; }
  .wave__fill { fill: var(--maroon); }
  .wave__line { fill: none; stroke: var(--red); stroke-width: 3; }

  .cattle {
    position: absolute; left: 372px; top: 18px; width: 128px; height: 80px;
    background: var(--red); border-radius: 10px 22px 8px 8px;
  }

  .person { position: absolute; left: 40px; top: 238px; color: var(--white); }
  .person__name { font-family: "Cinzel", serif; font-weight: 500; font-size: 20px; letter-spacing: 0.03em; }
  .person__role { font-size: 12px; margin-left: 150px; margin-top: -2px; }

  .contacts {
    position: absolute; left: 318px; top: 150px;
    list-style: none; color: var(--white); font-size: 11.5px;
  }
  .contacts li { display: flex; align-items: center; gap: 7px; margin-bottom: 8px; }
  .contacts li:first-child { letter-spacing: 0.18em; font-size: 13px; }
  .contacts svg { width: 12px; height: 12px; flex: none; fill: none; stroke: var(--white); stroke-width: 1.6; }
</style>
</head>
<body>

<section class="card card--back" aria-label="Business card back">
  <div class="brand">
    <span class="brand__dot"></span>
    <span class="brand__name">Coralvale<br>Meat Traders</span>
  </div>
</section>

<section class="card card--front" aria-label="Business card front">
  <svg class="wave" viewBox="0 0 540 310" preserveAspectRatio="none" aria-hidden="true">
    <path class="wave__fill" d="M0,212 C150,200 270,180 335,118 C385,72 455,66 540,62 L540,310 L0,310 Z"/>
    <path class="wave__line" d="M60,206 C150,190 230,176 285,160"/>
    <path class="wave__line" d="M380,84 C430,62 480,56 540,52"/>
  </svg>

  <div class="cattle" role="img" aria-label="Silhouette of a standing cow"></div>

  <div class="brand">
    <span class="brand__dot"></span>
    <span class="brand__name">Coralvale<br>Meat Traders</span>
  </div>

  <div class="person">
    <p class="person__name">DECLAN HARWOOD</p>
    <p class="person__role">Director</p>
  </div>

  <ul class="contacts">
    <li>
      <svg viewBox="0 0 12 12"><path d="M3 1 L5 3.5 L4 5 C5 7 6 8 7 8.5 L8.5 7.5 L11 9.5 L9.5 11 C5 11 1 7 1 2.5 Z"/></svg>
      0400-217-693
    </li>
    <li>
      <svg viewBox="0 0 12 12"><rect x="1" y="2.5" width="10" height="7"/><path d="M1 2.5 L6 6.5 L11 2.5"/></svg>
      info@coralvalemeat.com.au
    </li>
    <li>
      <svg viewBox="0 0 12 12"><circle cx="6" cy="6" r="5"/><path d="M1 6 H11 M6 1 C3.5 4 3.5 8 6 11 M6 1 C8.5 4 8.5 8 6 11"/></svg>
      www.coralvalemeat.com.au
    </li>
  </ul>
</section>

</body>
</html>
```